Flyer for a 1 day conference event - with our design elements

We need a two sided A4 flyer created for our 1 day conference, using our corporate design elements.

It is an exclusive event for high profile professional speakers, and it's important for the flyer to be engaging, professional and clean.

We want the prospective attendees to see how much value there is in the day and to feel the event cannot be missed.

I will need to be able to make small edits back and forth with the successful designer in order to get it just-right. (ie: It won't work if I only get access to 2-3 revisions... but don't worry - I don't intend to request an entire re-design)

Target Market(s)

High profile professional speakers

Industry/Entity Type

Event

Requirements
Must have
• Not too much clutter. Some of own design elements
Nice to have
• A large image/photo. Doesnt have to be of a microphone or stage or curtain (traditional speaker things) .. it could be something 'spring' like because it being held in Spring.
Should not have
• too many colours. too many different fonts. too much clutter.

```html
<!DOCTYPE html>
<html lang="en">
<head>
<meta charset="utf-8">
<title>The CSP Unconvention – Flyer</title>
<link rel="stylesheet" href="https://fonts.googleapis.com/css2?family=Lato:ital,wght@0,400;0,700;0,900;1,400;1,900&display=swap">
<style>
  :root {
    --navy: #1a3a7c;
    --blue: #1f5fa8;
    --sky: #4aa6dc;
    --pale: #d4e9f6;
    --ink: #1c1c1c;
    --white: #ffffff;
    --leaf: #7f8f6c;
    --mist: #c9cdc6;
  }
  html, body { margin: 0; padding: 0; overflow: hidden; background: var(--white); }
  .canvas { position: relative; width: 1200px; height: 851px; overflow: hidden; font-family: "Lato", sans-serif; color: var(--ink); }

  /* ---------- Front page ---------- */
  .front { position: absolute; left: 0; top: 0; width: 590px; height: 851px; overflow: hidden; }
  .front-photo { position: absolute; inset: 0;
    background: radial-gradient(ellipse at 45% 62%, #f4f5f2 0%, #dfe2dc 24%, var(--mist) 46%, var(--leaf) 80%, #5f6d4d 100%); }
  .front-swoosh { position: absolute; inset: 0; }
  .org-mark { position: absolute; left: 40px; top: 36px; width: 180px; }
  .org-dot { display: inline-block; width: 12px; height: 12px; border-radius: 50%; background: var(--blue); vertical-align: top; margin: 3px 6px 0 0; }
  .org-name { font-weight: 700; font-size: 15px; line-height: 1.1; color: var(--navy); display: inline-block; width: 140px; vertical-align: top; }
  .org-tag { font-weight: 700; font-size: 10px; color: var(--navy); margin: 6px 0 0 18px; }
  .front-title { position: absolute; left: 0; width: 590px; top: 262px; margin: 0; text-align: center; font-weight: 700; color: var(--navy); font-size: 31px; line-height: 1.25; }
  .no-word { position: absolute; left: 104px; top: 502px; transform: rotate(-90deg); transform-origin: left top; font-weight: 900; font-size: 70px; line-height: 40px; height: 40px; color: var(--white); white-space: nowrap; }
  .no-list { position: absolute; left: 146px; top: 396px; list-style: none; margin: 0; padding: 0; font-weight: 900; color: var(--navy); font-size: 21px; line-height: 28px; }
  .front-tagline { position: absolute; left: 326px; top: 740px; color: var(--white); font-weight: 900; font-size: 21px; line-height: 28px; text-shadow: 0 1px 3px rgba(0,0,0,.35); }
  .front-tagline .t2 { font-style: italic; }
  .front-arrow { position: absolute; left: 452px; top: 770px; }

  /* ---------- Back page ---------- */
  .back { position: absolute; left: 598px; top: 0; width: 602px; height: 851px; overflow: hidden; background: var(--white); }
  .back-swoosh { position: absolute; left: 0; top: 0; }
  .contact-line { position: absolute; left: 20px; top: 826px; transform: rotate(-90deg); transform-origin: left top; white-space: nowrap; font-weight: 700; font-size: 12px; color: var(--white); }
  .back-title { position: absolute; left: 32px; top: 20px; margin: 0; white-space: nowrap; color: var(--navy); line-height: 30px; }
  .back-title strong { font-weight: 700; font-size: 25px; }
  .back-title em { font-size: 13px; font-weight: 400; }

  .details { position: absolute; left: 109px; top: 62px; font-size: 9.5px; line-height: 1.35; }
  .details p { margin: 0 0 9px; }
  .details .lead { font-weight: 900; font-size: 10.5px; margin-bottom: 10px; }
  .price-stamp { position: absolute; left: 393px; top: 60px; transform: rotate(-5deg); font-size: 11px; line-height: 1.3; }
  .price-stamp .early { font-weight: 900; font-size: 11.5px; margin-bottom: 12px; }
  .price-underline { position: absolute; left: 360px; top: 132px; }

  .agenda { position: absolute; left: 108px; top: 172px; margin: 0; font-size: 9px; line-height: 12px; white-space: nowrap; }
  .section { position: absolute; left: 86px; width: 510px; }
  .section-head { display: flex; align-items: flex-end; gap: 3px; margin: 0 0 5px 0; height: 18px; font-weight: 900; font-size: 13px; line-height: 18px; color: var(--navy); text-transform: uppercase; white-space: nowrap; }
  .section-head svg { flex: none; }
  .item { margin: 0 0 7px 22px; font-size: 9px; line-height: 12px; white-space: nowrap; }
  .item h3 { margin: 0; font-weight: 700; font-size: 9px; line-height: 12px; color: var(--blue); }
  .item p { margin: 0; }
  .debate-lead { margin: 0 0 18px 22px; font-weight: 700; font-size: 9px; line-height: 12px; white-space: nowrap; }
  .debate-lead .bar { color: var(--blue); }
  .topics { margin: 0 0 10px 22px; font-size: 9px; line-height: 12px; white-space: nowrap; }
  .topics em { display: block; }
  .topics ul { list-style: none; margin: 0; padding: 0 0 0 34px; }
  .indented { margin-left: 56px; }
  .indented h3 { color: var(--ink); }
  .hypo { position: absolute; left: 418px; top: 500px; width: 128px; height: 78px; transform: rotate(-16deg); text-align: center; font-size: 8.4px; line-height: 1.2; }
  .hypo svg { position: absolute; left: -8px; top: -6px; }
  .hypo strong { display: block; font-weight: 900; font-size: 9.4px; padding-top: 8px; }
</style>
</head>
<body>
<div class="canvas">

  <!-- Front page -->
  <section class="front">
    <div class="front-photo" role="img" aria-label="Spring photograph: a white blossom with water droplets against soft green leaves"></div>
    <svg class="front-swoosh" width="590" height="851" viewBox="0 0 590 851" aria-hidden="true">
      <path d="M0 0 H590 V10 C450 40 320 80 200 120 C130 142 60 150 0 150 Z" fill="var(--white)"/>
      <path d="M200 120 C330 75 460 40 590 20 V0 H400 C360 30 290 80 200 120 Z" fill="var(--pale)" opacity=".9"/>
      <path d="M260 95 C380 45 490 20 590 10 V0 H460 C410 30 340 65 260 95 Z" fill="var(--sky)"/>
      <path d="M330 62 C430 25 520 8 590 2 V0 H430 Z" fill="var(--blue)"/>
      <path d="M0 150 C60 160 150 150 230 125 C160 160 80 175 0 178 Z" fill="var(--pale)" opacity=".7"/>
    </svg>
    <div class="org-mark">
      <span class="org-dot"></span><span class="org-name">Professional Speakers Guild of Australia</span>
      <div class="org-tag">Voices Worth Hearing</div>
    </div>
    <h1 class="front-title">THE CSP UNCONVENTION<br>for experienced, successful speakers</h1>
    <span class="no-word">NO</span>
    <ul class="no-list">
      <li>stars.</li>
      <li>keynotes.</li>
      <li>workshops.</li>
      <li>tweets.</li>
    </ul>
    <div class="front-tagline">
      <div class="t1">INSTANTLY INTIMATE</div>
      <div class="t2">Let’s get straight into it!</div>
    </div>
    <svg class="front-arrow" width="110" height="40" viewBox="0 0 110 40" aria-hidden="true">
      <path d="M4 8 C20 36 70 36 96 22" fill="none" stroke="var(--navy)" stroke-width="1.6"/>
      <path d="M86 14 L98 21 L88 31" fill="none" stroke="var(--navy)" stroke-width="1.6"/>
    </svg>
  </section>

  <!-- Back page -->
  <section class="back">
    <svg class="back-swoosh" width="602" height="851" viewBox="0 0 602 851" aria-hidden="true">
      <path d="M0 0 H30 C30 200 60 420 40 851 H0 Z" fill="var(--pale)"/>
      <path d="M0 60 C60 200 100 380 100 500 C100 640 80 760 60 851 H0 Z" fill="var(--pale)" opacity=".8"/>
      <path d="M0 110 C40 230 70 380 70 520 C70 650 55 760 50 851 H0 Z" fill="var(--sky)"/>
      <path d="M0 200 C30 300 50 430 48 560 C46 680 38 780 34 851 H0 Z" fill="var(--blue)"/>
      <path d="M0 300 C20 420 30 560 26 700 C24 770 20 820 18 851 H0 Z" fill="var(--navy)"/>
    </svg>
    <div class="contact-line">Contact Daniel to discuss: daniel@marlowtalks.com</div>

    <h1 class="back-title"><strong>THE CSP UNCONVENTION</strong><em> for experienced, successful speakers</em></h1>

    <div class="details">
      <p class="lead">No stars. No keynotes. No workshops. No tweets.</p>
      <p>Facilitator :: Daniel Marlow</p>
      <p>Venue :: xxx Melbourne</p>
      <p>November 5 :: 8:30am - 5pm<br>followed by an optional pub dinner</p>
    </div>
    <div class="price-stamp">
      <div class="early">Book before Sept 30 : $195</div>
      <div>After Sept 30 : $195<br>PLUS $100 donation to a charity<br>chosen by the group on the day</div>
    </div>
    <svg class="price-underline" width="160" height="24" viewBox="0 0 160 24" aria-hidden="true">
      <path d="M2 22 C60 14 110 6 154 2 L150 8 C100 12 50 18 2 22 Z" fill="var(--navy)"/>
    </svg>

    <p class="agenda">The day’s agenda will be made up of a couple of exercises from each of the three sections.</p>

    <div class="section" style="top:195px">
      <h2 class="section-head"><svg width="20" height="18" viewBox="0 0 20 18" aria-hidden="true"><path d="M1 10 L7 16 L19 1 L7 11 Z" fill="var(--blue)"/></svg>Instantly Intimate :: Let’s get straight into it.</h2>
      <div class="item"><h3>Why to Say, When to Say, How to Say No</h3><p>What policies and processes do you have – or need – for declining work you don’t really want to do?</p></div>
      <div class="item"><h3>How Much and To Who?</h3><p>How do you decide how much charity work to do, for who and on what basis – and how do you manage it?</p></div>
      <div class="item"><h3>Traveling Rituals</h3><p>What habits and rituals do you have when you travel – in the air, on the ground, in your hotel room – and why?</p></div>
      <div class="item"><h3>Step Inside My Office</h3><p>Five speakers give us a five minute super intimate look at how they manage their business.<br>No frills, no glam, just the basic day to day of it.</p></div>
      <div class="item"><h3>Looking After Yourself</h3><p>How do you manage the physical, mental and psycho-spiritual dangers of being a professional speaker?<br>How do you look after yourself?</p></div>
      <div class="item"><h3>Ask and Answer Five Questions</h3><p>Five minutes each with three other people in which you ask and answer five questions<br>(some given to you, some of your own). You can say Pass up to five times.</p></div>
    </div>

    <div class="section" style="top:453px">
      <h2 class="section-head"><svg width="20" height="18" viewBox="0 0 20 18" aria-hidden="true"><path d="M1 10 L7 16 L19 1 L7 11 Z" fill="var(--blue)"/></svg>Debate and Dissent :: Let’s get some friction and sport.</h2>
      <p class="debate-lead">Thumbite Debates <span class="bar">|</span> Three affirmative, three negative, one minute per person – go.</p>
      <div class="topics">
        <em>Topics will be generated on the day and may include:</em>
        <ul>
          <li>That motivational speakers were responsible for the GFC.</li>
          <li>That the PSGA has lost its way.</li>
          <li>That bureaus are underappreciated.</li>
          <li>That it is too easy to become a CSP.</li>
          <li>That ego has no place in speaking.</li>
        </ul>
      </div>
      <div class="item indented"><h3>Telling People What They Don’t Want To Hear</h3><p>Three people will each present a difficult truth to a hostile audience while we explore ways<br>of delivering more confronting, provocative or unpopular ideas and how we might better deal<br>with dissent or discomfort in the room.</p></div>
    </div>

    <div class="hypo">
      <svg width="144" height="90" viewBox="0 0 144 90" aria-hidden="true"><ellipse cx="72" cy="45" rx="69" ry="41" fill="none" stroke="var(--ink)" stroke-width="2.2"/></svg>
      <strong>Help Me Hypothetically</strong>
      Anonymous submissions<br>of ethical challenges<br>receive responses<br>and we discuss.
    </div>

    <div class="section" style="top:652px">
      <h2 class="section-head"><svg width="20" height="18" viewBox="0 0 20 18" aria-hidden="true"><path d="M1 10 L7 16 L19 1 L7 11 Z" fill="var(--blue)"/></svg>Immediate Insight :: Share what you know or see, fast.</h2>
      <div class="item"><h3>Blow My Trumpet For Me</h3><p>Get your promotional copy written by three other people. What does it say? What does it tell you?<br>What do you learn?</p></div>
      <div class="item"><h3>Emergency Presentation</h3><p>You are put into small groups – crack teams – to prepare a keynote from various criteria.<br>Ten minutes to prepare. Five minutes to present your outline.</p></div>
      <div class="item"><h3>Instant Unedited Product Review</h3><p>Get a super-efficient, ruthless critique of one of your products.</p></div>
      <div class="item"><h3>Show Me The Future</h3><p>Webinar, video channels, social pages, Blogging, microblogs, podcasts and ebooks – what is going on?<br>Which are you doing? Which are you resisting or declining? What’s next?</p></div>
    </div>
  </section>

</div>
</body>
</html>
```